Veltrium stationery design

Design stationery for us that fits with the colours of the logo. We are looking for letterheads, business cards etc. Something we can use for a prospectus and marketing presentations in power point. Must be completed in such a manner that it represents a corporate image for large enterprise clients and other large organisations. The company is a project assurance and monitoring company that works in all industries.

```html
<!DOCTYPE html>
<html lang="en">
<head>
<meta charset="utf-8">
<title>Veltrium stationery</title>
<link href="https://fonts.googleapis.com/css2?family=Montserrat:wght@400;500;700;800&family=Rubik:wght@400&display=swap" rel="stylesheet">
<style>
  :root {
    --backdrop: #b5babf;
    --paper: #ffffff;
    --ink: #111111;
    --black: #000000;
    --navy: #0a3582;
    --red: #f21d0a;
    --orange: #f4511e;
    --watermark: #e4e9f2;
  }
  * { margin: 0; padding: 0; box-sizing: border-box; }
  html, body { width: 1200px; height: 945px; overflow: hidden; }
  body { background: var(--backdrop); position: relative; font-family: "Montserrat", sans-serif; color: var(--ink); }

  .brand { display: flex; align-items: center; gap: 8px; font-family: "Montserrat", sans-serif; font-weight: 800; letter-spacing: 0.5px; }
  .brand-dot { border-radius: 50%; background: var(--red); flex: none; }

  /* Letterhead */
  .letterhead { position: absolute; left: 113px; top: 105px; width: 526px; height: 742px; background: var(--paper); box-shadow: 0 2px 6px rgba(0,0,0,0.25); overflow: hidden; }
  .letterhead-header { position: absolute; left: 0; top: 0; width: 100%; height: 96px; background: var(--black); color: #fff; font-family: "Rubik", sans-serif; }
  .letterhead-header .brand { position: absolute; left: 34px; top: 37px; font-size: 17px; color: var(--navy); }
  .letterhead-header .brand-dot { width: 14px; height: 14px; }
  .divider { position: absolute; top: 36px; width: 1px; height: 24px; background: #fff; }
  .header-contact { position: absolute; font-size: 11px; line-height: 15px; display: flex; gap: 7px; align-items: flex-start; white-space: nowrap; }
  .header-contact svg { width: 9px; height: 9px; margin-top: 3px; flex: none; }
  .header-contact.address-block { line-height: 11px; }
  .header-contact.address-block svg { margin-top: 1px; }
  .watermark { position: absolute; left: 0; width: 100%; top: 345px; text-align: center; font-weight: 800; font-size: 64px; color: var(--watermark); letter-spacing: 3px; }
  .band { position: absolute; bottom: 0; height: 13px; }
  .letterhead .band-red { left: 0; width: 272px; background: var(--red); clip-path: polygon(0 0, 100% 0, 94% 100%, 0 100%); }
  .letterhead .band-navy { right: 0; width: 255px; background: var(--navy); clip-path: polygon(6% 0, 100% 0, 100% 100%, 0 100%); }

  /* Business cards */
  .card { position: absolute; border-radius: 17px; overflow: hidden; box-shadow: 0 3px 8px rgba(0,0,0,0.3); }
  .card-front { left: 684px; top: 202px; width: 421px; height: 241px; background: var(--paper); }
  .card-front .brand { position: absolute; left: 50px; top: 48px; font-size: 30px; color: var(--navy); }
  .card-front .brand-dot { width: 26px; height: 26px; }
  .person { position: absolute; right: 21px; top: 117px; text-align: right; }
  .person-name { font-weight: 700; font-size: 16.5px; color: var(--navy); letter-spacing: 0.3px; }
  .person-role { font-weight: 500; font-size: 11.5px; margin-top: 2px; letter-spacing: 0.4px; }
  .tab { position: absolute; right: 0; top: 121px; width: 5px; height: 29px; background: var(--navy); }
  .rule { position: absolute; left: 29px; right: 21px; top: 160px; height: 1px; background: var(--ink); }
  .contacts { position: absolute; left: 27px; top: 172px; list-style: none; font-size: 10.5px; }
  .contacts li { display: flex; align-items: center; gap: 10px; height: 16px; margin-bottom: 1px; }
  .contacts svg { width: 12px; height: 12px; flex: none; }
  .address { position: absolute; right: 21px; top: 189px; text-align: right; font-size: 10.5px; line-height: 14px; }
  .card-front .band { height: 10px; }
  .card-front .band-red { left: 0; width: 205px; background: var(--red); clip-path: polygon(0 0, 100% 0, 93% 100%, 0 100%); }
  .card-front .band-navy { right: 0; width: 212px; background: var(--navy); clip-path: polygon(6% 0, 100% 0, 100% 100%, 0 100%); }

  .card-back { left: 688px; top: 509px; width: 412px; height: 235px; background: var(--black); }
  .card-back .brand { position: absolute; left: 0; right: 0; top: 104px; justify-content: center; font-size: 30px; color: var(--orange); }
  .card-back .brand-dot { width: 26px; height: 26px; }
</style>
</head>
<body>

<section class="letterhead">
  <header class="letterhead-header">
    <div class="brand"><span class="brand-dot"></span>VELTRIUM</div>
    <span class="divider" style="left:219px"></span>
    <div class="header-contact" style="left:235px; top:33px">
      <svg viewBox="0 0 24 24"><path fill="#f21d0a" d="M6.6 10.8a15 15 0 0 0 6.6 6.6l2.2-2.2c.3-.3.7-.4 1-.2 1.1.4 2.3.6 3.6.6.6 0 1 .4 1 1V20c0 .6-.4 1-1 1A17 17 0 0 1 3 4c0-.6.4-1 1-1h3.5c.6 0 1 .4 1 1 0 1.3.2 2.5.6 3.6.1.3 0 .7-.2 1z"/></svg>
      <span>044-555 210 384</span>
    </div>
    <div class="header-contact" style="left:235px; top:49px">
      <svg viewBox="0 0 24 24"><path fill="#f21d0a" d="M2 5h20v14H2z"/><path d="M2 5l10 8 10-8" fill="none" stroke="#000" stroke-width="1.5"/></svg>
      <span>info@veltrium.co</span>
    </div>
    <span class="divider" style="left:360px"></span>
    <div class="header-contact" style="left:367px; top:30px">
      <svg viewBox="0 0 24 24"><circle cx="12" cy="12" r="10" fill="none" stroke="#f21d0a" stroke-width="2.5"/><path d="M2 12h20M12 2c3 3 3 17 0 20M12 2c-3 3-3 17 0 20" fill="none" stroke="#f21d0a" stroke-width="2"/></svg>
      <span>www.veltriumgrp.com</span>
    </div>
    <div class="header-contact address-block" style="left:367px; top:48px">
      <svg viewBox="0 0 24 24"><path fill="#f21d0a" d="M12 2a7 7 0 0 0-7 7c0 5 7 13 7 13s7-8 7-13a7 7 0 0 0-7-7zm0 9.5a2.5 2.5 0 1 1 0-5 2.5 2.5 0 0 1 0 5z"/></svg>
      <span>27 Harbour Row, Eastmere<br>Eastmere Land, 60418</span>
    </div>
  </header>
  <div class="watermark">VELTRIUM</div>
  <span class="band band-red"></span>
  <span class="band band-navy"></span>
</section>

<section class="card card-front">
  <div class="brand"><span class="brand-dot"></span>VELTRIUM</div>
  <div class="person">
    <p class="person-name">DANIEL HARWOOD</p>
    <p class="person-role">MANAGING DIRECTOR</p>
  </div>
  <span class="tab"></span>
  <span class="rule"></span>
  <ul class="contacts">
    <li><svg viewBox="0 0 24 24"><path fill="#f21d0a" d="M6.6 10.8a15 15 0 0 0 6.6 6.6l2.2-2.2c.3-.3.7-.4 1-.2 1.1.4 2.3.6 3.6.6.6 0 1 .4 1 1V20c0 .6-.4 1-1 1A17 17 0 0 1 3 4c0-.6.4-1 1-1h3.5c.6 0 1 .4 1 1 0 1.3.2 2.5.6 3.6.1.3 0 .7-.2 1z"/></svg>044-555 210 384</li>
    <li><svg viewBox="0 0 24 24"><path fill="#f21d0a" d="M2 5h20v14H2z"/><path d="M2 5l10 8 10-8" fill="none" stroke="#fff" stroke-width="1.5"/></svg>info@veltrium.co</li>
    <li><svg viewBox="0 0 24 24"><circle cx="12" cy="12" r="10" fill="none" stroke="#f21d0a" stroke-width="2.5"/><path d="M2 12h20M12 2c3 3 3 17 0 20M12 2c-3 3-3 17 0 20" fill="none" stroke="#f21d0a" stroke-width="2"/></svg>www.veltriumgrp.com</li>
  </ul>
  <p class="address">27 Harbour Row, Eastmere<br>60418, Eastmere Land</p>
  <span class="band band-red"></span>
  <span class="band band-navy"></span>
</section>

<section class="card card-back">
  <div class="brand"><span class="brand-dot"></span>VELTRIUM</div>
</section>

</body>
</html>
```